Maren Holt Luxury Wellness Profile Booklet

I am a luxury wellness property agent and would like to create my personal profile booklet. I want this to feel luxurious, minimalist, informative and the philosophy behind wellness and property the cPAGE 1 — THE COVER

Very minimal.

MAREN HOLT

LUXURY WELLNESS PROPERTY

PROPERTY • WELLNESS • LIFESTYLE

Fenwick Dale Coastline Group

Large photograph of you — preferably walking through a beautiful waterfront property or standing naturally within an architectural setting.

At the bottom:

Hope Island • Sanctuary Cove • Helensvale

Small Fenwick Dale logo.

PAGE 2 — THE OPENING STATEMENT

A beautiful full-page lifestyle photograph.

Overlaid:

WHERE PROPERTY
MEETS WELLBEING

“A home is more than an address. It is the environment in which life unfolds.”

Then a short introduction:

Opening Profile

I believe the most exceptional properties are not defined simply by their architecture, address or price.

They are defined by how they make you feel.

Natural light. Water views. Privacy. Green space. Indoor-outdoor living. A place to unwind, entertain, recharge and reconnect.

My approach to luxury property brings these elements together — combining strategic real estate expertise with a genuine understanding of wellness, lifestyle and the way people want to live today.

Because when we understand the lifestyle behind the property, we can create a more compelling story around it.

PAGE 3 — MEET MAREN

Large portrait of you on one side.

Other side:

MEET MAREN

20+ YEARS OF PROPERTY EXPERIENCE

Commercial
Residential
Project Sales
Luxury & Lifestyle Property

Then:

About Maren

With more than 20 years' experience across commercial, residential and project sales, I have built my career around relationships, strategic marketing and delivering exceptional outcomes for my clients.

My approach is warm, considered and highly personal.

I believe sellers deserve more than a listing campaign. They deserve a clear strategy, honest communication and an agent who understands what makes their property valuable — both financially and emotionally.

Today, my focus is luxury lifestyle property across the Northern Gold Coast, with a particular passion for Hope Island, Sanctuary Cove and selected waterfront gated estates in Helensvale.

PAGE 4 — WHY WELLNESS?

This is where your differentiation becomes really powerful.

Full-bleed photograph of:

pool
outdoor entertaining
greenery
water
spa
wellness room
person walking beside water
WELLNESS IS THE NEW LUXURY

Then:

Wellness Philosophy

Luxury has evolved.

Today, luxury is not only about beautiful finishes, expansive living spaces or an impressive address.

It is privacy.

It is waking to water.

It is natural light flooding through the home.

It is having space to breathe.

It is stepping outside into nature, walking along the water, enjoying a morning swim, entertaining beside the pool or creating a private sanctuary at home.

These lifestyle elements increasingly shape the way buyers experience and value a property.

This is where my passion for wellness becomes part of my property approach.

PAGE 5 — MY WELLNESS JOURNEY

This page makes the wellness positioning credible rather than simply being a marketing slogan.

MY WELLNESS JOURNEY

You could use 3 small photographs:

BLOOMTOT CO
SOLACE WELLNESS CENTRE
LUXURY WELLNESS PROPERTY

Copy:

Wellness Journey

My connection with wellness began outside of real estate.

After stepping away from property, I founded Bloomtot Co, developing an organic children's nutritional product with a focus on natural ingredients and wellbeing.

I later launched Solace Wellness Centre, further deepening my understanding of wellness, health-conscious lifestyles and the importance of creating environments that support how we live.

Today, I bring that perspective back into property.

I see homes differently — not simply as buildings, but as environments for living, restoring, entertaining and thriving.

PAGE 6 — THE MAREN HOLT DIFFERENCE

This should be one of your strongest pages.

A DIFFERENT WAY OF SEEING PROPERTY

Use six elegant icons or small images:

01 — LIFESTYLE

I look beyond the floor plan to understand how buyers will actually experience the home.

02 — WELLNESS

I identify the spaces and features that contribute to wellbeing and lifestyle.

03 — PRESENTATION

I create a campaign that makes the property feel aspirational, memorable and emotionally engaging.

04 — STORY

Every exceptional property has a story. I find it, refine it and communicate it.

05 — STRATEGY

From positioning and buyer targeting to campaign execution and negotiation, every element has a purpose.

06 — RELATIONSHIPS

Trust, transparency and communication remain at the centre of every campaign.

PAGE 7 — YOUR PROPERTY STORY

This could be a beautiful editorial spread.

EVERY HOME HAS A STORY

Then:

My role is to discover what makes yours extraordinary.

Three questions:

WHAT MAKES YOUR PROPERTY DIFFERENT?

Architecture?
Waterfront?
Views?
Privacy?
Garden?
Location?

HOW DOES IT MAKE PEOPLE FEEL?

Calm?
Inspired?
Connected?
Entertained?
Relaxed?

WHO WILL FALL IN LOVE WITH IT?

Families?
Executives?
Downsizers?
Boaties?
Golfers?
Wellness-focused buyers?
Lifestyle purchasers?

Then:

I turn these answers into your property's story.

PAGE 8 — YOUR NORTHERN GOLD COAST

Beautiful aerial/waterfront image.

MY MARKET

HOPE ISLAND

SANCTUARY COVE

HELENSVALE

WATERFRONT & GATED ESTATES

Copy:

Northern Gold Coast

I specialise in the lifestyle-driven property market of the Northern Gold Coast.

From the waterfront homes and private enclaves of Hope Island and Sanctuary Cove to the established gated estates of Helensvale, I understand the lifestyle characteristics that attract buyers to this part of the Gold Coast.

Having personally experienced the lifestyle of these communities, I understand that buyers are often purchasing far more than a house.

They are buying a way of life.

PAGE 9 — THE WELLNESS PROPERTY

This could become your signature page.

WHAT MAKES A WELLNESS HOME?

Use a sophisticated grid:

WATER
Pools • Waterfront • Marina • Water views

NATURE
Green space • Gardens • Reserve outlooks • Walking trails

LIGHT
Natural light • Orientation • Open spaces

MOVEMENT
Walking • Golf • Boating • Outdoor living

RESTORATION
Spa • Sauna • Cold plunge • Retreat spaces

CONNECTION
Entertaining • Family • Indoor/outdoor living

Bottom:

The most desirable luxury is often the way a home makes you feel.

PAGE 10 — THE SELLING EXPERIENCE
YOUR HOME. YOUR STORY. YOUR CAMPAIGN.

I would make this a simple six-stage journey:

01 — DISCOVER
Understand your property, your goals and your lifestyle.

↓

02 — POSITION
Establish the property's unique market position.

↓

03 — PREPARE
Presentation, styling and strategic recommendations.

↓

04 — CREATE
Photography, film, editorial storytelling and digital marketing.

↓

05 — CONNECT
Targeted buyer engagement and database activation.

↓

06 — NEGOTIATE
Strategic negotiation designed to maximise the opportunity.

PAGE 11 — THE POWER OF PRESENTATION

Large before/after style photography.

FIRST IMPRESSIONS ARE EVERYTHING

Copy:

We don't get a second opportunity to create a first impression.

Then explain your approach to:

styling
photography
cinematic video
twilight imagery
aerial photography
lifestyle storytelling
digital advertising
targeted database marketing
buyer follow-up
auction strategy

Importantly, don't make this page feel like a generic list of marketing products.

Frame everything around:

Creating desire before creating urgency.
PAGE 12 — PROVEN RESULTS

Now introduce your actual results.

RESULTS THAT BUILD CONFIDENCE

Use your strongest results as elegant case studies.

For example:
4183 Palmetto Drive, Hope Island
$3,850,000
34 Days On The Market

$2.90M
71 Heron Bay Boulevard, Helensvale
Sold within 45 days

Include your result and the property's story.

$2.15M

3/9 Heron Bay Boulevard

Waterfront Villa

Then potentially:

28 DAYS

5419 Quaywood Boulevard, Hope Island

Under contract following relaunch

If a result subsequently changed because the contract fell through, be careful about how you describe the current status. We can make this page completely accurate to the final outcome.

PAGE 13 — THE FENWICK DALE ADVANTAGE

This is where you let the brand support you, rather than letting the booklet become a Fenwick Dale corporate brochure.

PERSONAL SERVICE.
NATIONAL REACH.

Then a short statement about your Fenwick Dale platform.

You could include:

POWERFUL BUYER DATABASE

LUXURY PROPERTY MARKETING

AUCTION EXPERTISE

DIGITAL REACH

LOCAL KNOWLEDGE

NATIONAL NETWORK

And a short line:

The personal attention of a specialist agent, supported by the strength of a globally recognised property network.

PAGE 14 — WHAT YOU CAN EXPECT FROM ME

This page is very important for your seller proposition.

MY PROMISE TO YOU

TRANSPARENCY

Clear advice, honest feedback and no unnecessary promises.

COMMUNICATION

You will know what is happening throughout your campaign.

STRATEGY

Every decision is made with your property, market and objectives in mind.

ATTENTION TO DETAIL

Your home deserves meticulous preparation and presentation.

PERSONAL SERVICE

You deal directly with me throughout your campaign.

RESULT FOCUS

My role is to create the strongest possible environment for a successful sale.

PAGE 15 — THE CLOSING PAGE

This should be very luxurious and emotional.

Beautiful photograph of water at sunset / luxury pool / Hope Island lifestyle.

YOUR HOME.
YOUR NEXT CHAPTER.

Then:

Closing Statement

Selling a home is rarely just a transaction.

It is the closing of one chapter and the beginning of another.

My role is to make the journey feel considered, strategic and personal — while creating the strongest possible opportunity for your property in the marketplace.

Thank you for considering me to represent your home.

I would be honoured to tell its story.

Then your details:

MAREN HOLT

Luxury Wellness Property

0412 557 830

BACK COVER

Keep it extremely clean.

Your photograph or perhaps a beautiful Gold Coast waterfront image.

MAREN HOLT

LUXURY WELLNESS PROPERTY

0412 557 830

Fenwick Dale logoollaboration. I can send a full brief if required.

Target Market(s)

Luxury Property Owners

Industry/Entity Type

Wellness Luxury Real Estate Lifestyle

Requirements
Must have
• A luxurious minimalist clean feel

```html
<!DOCTYPE html>
<html lang="en">
<head>
<meta charset="utf-8">
<title>Maren Holt — Luxury Wellness Profile Booklet</title>
<link rel="stylesheet" href="https://fonts.googleapis.com/css2?family=Playfair+Display:wght@400;500&family=Outfit:wght@300;400;500;600&display=swap">
<style>
  :root {
    --stage: #8c8c8c;
    --paper: #f4f0e7;
    --paper-white: #f7f6f2;
    --teal: #1f4d48;
    --ink: #1f2322;
    --body: #4a4a47;
    --gold: #b38a58;
    --photo-sand: #e3d3c1;
    --photo-stone: #cbb8a4;
    --photo-green: #4d5b3a;
    --photo-dusk: #b27a45;
    --serif: "Playfair Display", Georgia, serif;
    --sans: "Outfit", Helvetica, Arial, sans-serif;
  }
  * { margin: 0; padding: 0; box-sizing: border-box; }
  html, body { width: 1200px; height: 800px; overflow: hidden; }
  body { background: var(--stage); font-family: var(--sans); color: var(--body); position: relative; }

  .spread { position: absolute; left: 100px; width: 1000px; height: 360px; display: flex; box-shadow: 0 10px 28px rgba(0,0,0,.25); }
  .spread--covers { top: 30px; }
  .spread--inside { top: 410px; }
  .page { position: relative; width: 500px; height: 360px; overflow: hidden; }
  .page--cream { background: var(--paper); }
  .page--white { background: var(--paper-white); }
  .page--left { box-shadow: inset -14px 0 18px -14px rgba(0,0,0,.18); }
  .page--right { box-shadow: inset 14px 0 18px -14px rgba(0,0,0,.14); }

  .eyebrow { font-family: var(--sans); font-size: 6px; letter-spacing: .08em; text-transform: uppercase; color: var(--teal); }
  .rule { display: block; width: 28px; height: 1px; background: var(--gold); }
  .serif-head { font-family: var(--serif); font-weight: 400; color: var(--ink); line-height: 1.02; }
  .copy p { font-size: 6.4px; line-height: 1.5; color: var(--body); font-weight: 300; margin-bottom: 6px; }
  .page-number { position: absolute; width: 11px; height: 11px; border-radius: 50%; background: var(--gold); color: #fff; font-size: 6px; display: flex; align-items: center; justify-content: center; }

  .photo { position: absolute; }

  /* Back cover / closing */
  .closing { padding: 34px 40px; }
  .closing__shade { position: absolute; right: 0; top: 0; width: 260px; height: 100%; background: radial-gradient(ellipse at 70% 35%, rgba(170,160,145,.28), rgba(244,240,231,0) 65%); }
  .closing .rule { margin: 7px 0 10px; }
  .closing__title { font-size: 25px; width: 260px; }
  .closing .copy { width: 220px; margin-top: 16px; }
  .closing__divider { margin: 14px 0 10px; }
  .closing__sign { position: absolute; left: 40px; bottom: 32px; }
  .closing__name { font-family: var(--serif); font-size: 11px; color: var(--ink); margin-bottom: 3px; }
  .closing__detail { font-size: 6.6px; color: var(--teal); line-height: 1.35; font-weight: 500; }

  /* Cover */
  .cover__text { position: absolute; left: 26px; top: 36px; width: 160px; }
  .cover__text .rule { margin: 6px 0 12px; }
  .cover__name { font-size: 40px; line-height: .95; }
  .cover__role { margin-top: 22px; font-size: 7.4px; font-weight: 600; letter-spacing: .02em; color: var(--teal); }
  .cover__tag { margin-top: 22px; font-family: var(--serif); font-size: 7.4px; line-height: 1.4; color: var(--body); }
  .cover__brand { position: absolute; left: 26px; bottom: 48px; display: flex; align-items: center; gap: 6px; }
  .cover__brand-mark { width: 24px; height: 24px; background: var(--gold); }
  .cover__brand-name { font-size: 6.6px; color: var(--ink); font-weight: 400; }
  .cover__places { position: absolute; left: 26px; bottom: 26px; font-size: 5.8px; font-weight: 600; color: var(--teal); letter-spacing: .03em; }
  .cover__photo { right: 18px; top: 18px; width: 280px; height: 324px; background: linear-gradient(160deg, #efe7dc 0%, var(--photo-sand) 45%, var(--photo-stone) 100%); }

  /* Opening statement */
  .opening__photo { left: 0; top: 0; width: 500px; height: 150px; background: linear-gradient(180deg, #c59a5e 0%, var(--photo-dusk) 25%, var(--photo-green) 60%, #6f7f88 85%, #c7c1b6 100%); }
  .opening__intro { position: absolute; left: 26px; top: 168px; width: 190px; }
  .opening__intro .rule { margin: 5px 0 9px; }
  .opening__title { font-size: 19px; }
  .opening__intro .copy { margin-top: 12px; }
  .opening__intro .copy .rule { margin: 0 0 7px; }
  .opening__quote { position: absolute; left: 240px; top: 166px; width: 220px; font-size: 8px; font-weight: 600; line-height: 1.35; color: var(--teal); }
  .opening__more { position: absolute; left: 240px; top: 214px; width: 230px; }
  .opening .page-number { right: 24px; bottom: 22px; }

  /* Meet */
  .meet__photo { left: 18px; top: 18px; width: 236px; height: 324px; background: linear-gradient(170deg, #ece6dd 0%, #e2d9cd 50%, #d8cbbb 100%); }
  .meet__text { position: absolute; left: 272px; top: 30px; width: 204px; }
  .meet__text .rule { margin: 5px 0 8px; }
  .meet__title { font-size: 19px; }
  .meet__title-rule { margin-top: 7px !important; }
  .meet__sectors { display: grid; grid-template-columns: 1fr 1.5fr; gap: 2px 10px; margin: 6px 0 6px; list-style: none; }
  .meet__sectors li { font-size: 6.4px; color: var(--teal); }
  .meet__sectors li::before { content: "• "; }
  .meet__line { height: 1px; background: var(--gold); opacity: .6; margin-bottom: 10px; }
  .meet .page-number { right: 24px; bottom: 22px; }
</style>
</head>
<body>

<section class="spread spread--covers">
  <article class="page page--cream page--left closing">
    <div class="closing__shade"></div>
    <p class="eyebrow">Property · Wellness · Lifestyle</p>
    <span class="rule"></span>
    <h2 class="serif-head closing__title">Your Home Your Next Chapter</h2>
    <span class="rule closing__divider"></span>
    <div class="copy">
      <p>Selling a home is rarely just a transaction. It is the closing of one chapter and the beginning of another.</p>
      <p>My role is to make the journey feel considered, strategic and personal - while creating the strongest possible opportunity for your property in the marketplace.</p>
      <p>Thank you for considering me to represent your home. I would be honoured to tell its story.</p>
    </div>
    <div class="closing__sign">
      <p class="closing__name">MAREN HOLT</p>
      <p class="closing__detail">Luxury Wellness Property<br>Fenwick Dale Coastline Group<br>0412 557 830</p>
    </div>
  </article>

  <article class="page page--cream page--right cover">
    <div class="cover__text">
      <p class="eyebrow">Property · Wellness · Lifestyle</p>
      <span class="rule"></span>
      <h1 class="serif-head cover__name">MAREN<br>HOLT</h1>
      <p class="cover__role">LUXURY WELLNESS PROPERTY</p>
      <p class="cover__tag">Luxury Lifestyle &amp; Wellness<br>Property Specialist</p>
    </div>
    <div class="cover__brand">
      <span class="cover__brand-mark"></span>
      <span class="cover__brand-name">Fenwick Dale Coastline Group</span>
    </div>
    <p class="cover__places">HOPE ISLAND • SANCTUARY COVE • HELENSVALE</p>
    <div class="photo cover__photo" role="img" aria-label="Portrait of Maren Holt walking down a staircase in a light architectural home"></div>
  </article>
</section>

<section class="spread spread--inside">
  <article class="page page--white page--left opening">
    <div class="photo opening__photo" role="img" aria-label="Waterfront home at sunset with pool, trees and a moored boat"></div>
    <div class="opening__intro">
      <p class="eyebrow">Opening Statement</p>
      <span class="rule"></span>
      <h2 class="serif-head opening__title">Where Property<br>Meets Wellbeing</h2>
      <div class="copy">
        <span class="rule"></span>
        <p>I believe the most exceptional properties are not defined simply by their architecture, address or price. They are defined by how they make you feel.</p>
        <p>Natural light. Water views. Privacy. Green space. Indoor-outdoor living. A place to unwind, entertain, recharge and reconnect.</p>
        <p>My approach to luxury property brings these elements together - combining strategic real estate expertise with a genuine</p>
      </div>
    </div>
    <p class="opening__quote">“A home is more than an address.<br>It is the environment in which life unfolds.”</p>
    <div class="opening__more copy">
      <p>understanding of wellness, lifestyle and the way people want to live today.</p>
      <p>Because when we understand the lifestyle behind the property, we can create a more compelling story around it.</p>
    </div>
    <span class="page-number">2</span>
  </article>

  <article class="page page--white page--right meet">
    <div class="photo meet__photo" role="img" aria-label="Portrait of Maren Holt seated in a bright neutral living room"></div>
    <div class="meet__text">
      <p class="eyebrow">Meet Maren</p>
      <span class="rule"></span>
      <h2 class="serif-head meet__title">20+ Years Of<br>Property<br>Experience</h2>
      <span class="rule meet__title-rule"></span>
      <ul class="meet__sectors">
        <li>Commercial</li>
        <li>Project Sales</li>
        <li>Residential</li>
        <li>Luxury &amp; Lifestyle Property</li>
      </ul>
      <div class="meet__line"></div>
      <div class="copy">
        <p>With more than 20 years' experience across commercial, residential and project sales, I have built my career around relationships, strategic marketing and delivering exceptional outcomes for my clients.</p>
        <p>My approach is warm, considered and highly personal.</p>
        <p>I believe sellers deserve more than a listing campaign. They deserve a clear strategy, honest communication and an agent who understands what makes their property valuable — both financially and emotionally.</p>
        <p>Today, my focus is luxury lifestyle property across the Northern Gold Coast, with a particular passion for Hope Island, Sanctuary Cove and selected waterfront gated estates in Helensvale.</p>
      </div>
    </div>
    <span class="page-number">3</span>
  </article>
</section>

</body>
</html>
```